Vendro-s / stay-rooted -> Align your thoughts and emotions with world peace

[En español at the end] Very good! Thank you for showing interest in our project :) We need a logo design and web design for a foundation based in Barcelona. Our goal is to work with people's psychology and philosophy to make their lives happier as well as the rest of the world, because we believe we can align them. The name of the foundation is "vendro-s" (véndrose), which comes to say that there is a way to align a series of concepts that take us from the peace and inner happiness of the individual to world peace and happiness. Very much in the line of Orrin Thale's quotation: "All the problems of humanity derive from that we do not know how to remain alone and quiet in a room". The concepts we want to align are the following, and in this order: Inner Peace Practical Philosophy Emotional Intelligence Critical Thinking Social Justice Conflict Resolution World Peace We enclose a couple of possible logo and web ideas, very grotesque and rudimentary. We are sure that you will be able to capture the idea and improve it in such a way that the idea will win with your contribution. Thank you very much in advance! Ah! And, vendro-s :-) -------------- Hi! Thanks for paying attention to this project! We are looking for a logo and web design for an association whose goal is to work with the psychology and philosophy of people in order to make their life happier as well as the happiness of the rest of the world. The name of the organization is "vendro-s" (get aligned) meaning that we can align ourselves with the next concepts (in this order): inner peace - practical philosophy - emotional intelligence - critical thinking - social justice - conflict resolution - global Peace Find some basic ideas that you might find in order to grasp what we are looking for, but feel free to add your own contribution, I am sure you can surprise us! :) Thank you in advance, Get aligned!

Project Deadline Extended Reason: Deadline extension conceded, however, it is highly recommended to have the final design by Tuesday 23rd of May at 5 pm, UTC + 1. Extension of the granted deadline, however, it is highly recommended to have the final design on Tuesday, May 23 at 5:00 p.m. (local Spain). Added Monday, May 22, 2017

Target Market(s)

We addressed mainly middle-class people with concerns for personal development. In the medium term, we plan to cover the spectrum of companies with training courses for their staff. The first project that we are sure will be carried out is the application of critical thinking for adolescents and young people.

Logo Text

Vendr-s

Number of Pages Required

1 page

Font styles to use
Sans Serif

Colors
3176b5
f37122

Requirements
Must have
• The essential elements are relatively abstract and numerous. Those exposed before: Inner Peace, Practical Philosophy, Emotional Intelligence, Critical Thinking, Social Justice, Conflict Resolution, World Peace. Probably the most striking or relevant will be two: emotional intelligence and critical thinking. The next level would be occupied by inner peace through meditation and introspection. And in the last level the other three.
Nice to have
• We want to transmit integrity and transparency, which in turn will be pillars of the educational and philosophical methods that we will teach. Empathy and compassion are also key. We have marked some colors, but still feel free to use another / others in your design. Sure you have great ideas :-) and we are looking forward to seeing them
Should not have
• We want to avoid at all costs the sensation of pseudoscience and volatility. Our values ​​are deep and we prefer to die rather than transmit an ambiguous, wrong, superfluous or interested message (in the sense of chaquetero).

```html
<!DOCTYPE html>
<html lang="en">
<head>
<meta charset="UTF-8">
<title>Vendro-s — Align your thoughts and emotions with world peace</title>
<meta name="description" content="Vendro-s, a Barcelona foundation aligning inner peace, practical philosophy, emotional intelligence, critical thinking, social justice, conflict resolution and world peace.">
<link rel="stylesheet" href="https://fonts.googleapis.com/css2?family=Baloo+2:wght@400;500;600;700&display=swap">
<style>
  :root {
    --sky-top: #8db2ee;
    --sky-mid: #a9cdf3;
    --sky-light: #b6d9f3;
    --sea-band: rgba(143, 202, 240, 0.55);
    --sand: rgba(205, 232, 250, 0.9);
    --white: #ffffff;
    --white-soft: rgba(255, 255, 255, 0.92);
    --button-pink: #e2c6fb;
    --button-blue: #9dbdfb;
    --button-shadow: rgba(90, 120, 200, 0.25);
  }
  * { margin: 0; padding: 0; box-sizing: border-box; }
  html, body {
    width: 1200px;
    height: 783px;
    overflow: hidden;
  }
  body {
    position: relative;
    font-family: "Baloo 2", sans-serif;
    color: var(--white);
  }
  .hero-photo {
    position: absolute;
    inset: 0;
    background:
      linear-gradient(180deg, rgba(255,255,255,0) 0%, rgba(255,255,255,0) 48%, var(--sea-band) 55%, rgba(170,214,246,0.4) 66%, var(--sand) 100%),
      linear-gradient(100deg, var(--sky-top) 0%, var(--sky-mid) 55%, var(--sky-light) 100%);
  }
  .site-nav {
    position: absolute;
    top: 26px;
    right: 48px;
    display: flex;
    gap: 12px;
  }
  .site-nav a {
    color: var(--white);
    text-decoration: none;
    font-size: 16px;
    font-weight: 600;
    line-height: 24px;
    padding: 0 8px 6px;
    border-bottom: 2px solid transparent;
  }
  .site-nav a.is-active { border-bottom-color: var(--white); }
  .brand {
    position: absolute;
    top: 226px;
    left: 0;
    width: 100%;
    display: flex;
    justify-content: center;
    align-items: center;
    gap: 24px;
  }
  .brand-dot {
    width: 68px;
    height: 68px;
    border-radius: 50%;
    border: 6px solid var(--white);
  }
  .brand-name {
    font-size: 90px;
    font-weight: 500;
    line-height: 1;
    letter-spacing: 1px;
  }
  .hero-copy {
    position: absolute;
    left: 94px;
    top: 423px;
  }
  .hero-title {
    font-size: 44px;
    font-weight: 700;
    line-height: 1;
    letter-spacing: 0.5px;
  }
  .hero-lead {
    margin-top: 14px;
    font-size: 21px;
    font-weight: 400;
    line-height: 33px;
    color: var(--white-soft);
  }
  .cta-button {
    display: inline-block;
    margin-top: 34px;
    width: 166px;
    height: 52px;
    line-height: 54px;
    text-align: center;
    font-size: 15px;
    font-weight: 600;
    letter-spacing: 0.5px;
    color: var(--white);
    text-decoration: none;
    background: linear-gradient(90deg, var(--button-pink), var(--button-blue));
    box-shadow: 0 4px 14px var(--button-shadow);
  }
  .scroll-cue {
    position: absolute;
    left: 588px;
    top: 684px;
  }
</style>
</head>
<body>
  <div class="hero-photo" role="img" aria-label="Photo of a woman meditating on a sunny beach by the sea, evoking inner peace, under a soft blue tint"></div>

  <nav class="site-nav">
    <a href="#" class="is-active">Home</a>
    <a href="#">About Us</a>
    <a href="#">Products</a>
    <a href="#">Contact</a>
  </nav>

  <div class="brand">
    <span class="brand-dot"></span>
    <span class="brand-name">Vendro-s</span>
  </div>

  <section class="hero-copy" aria-label="Align inner peace, practical philosophy, emotional intelligence, critical thinking, social justice, conflict resolution and world peace">
    <h1 class="hero-title">Get to know us a bit better.</h1>
    <p class="hero-lead">Join us now and learn new ways.</p>
    <a href="#" class="cta-button">CALL TO ACTION</a>
  </section>

  <svg class="scroll-cue" width="24" height="40" viewBox="0 0 24 40" aria-label="Scroll down">
    <rect x="2" y="5" width="20" height="33" rx="4" fill="none" stroke="#ffffff" stroke-width="2"/>
    <line x1="12" y1="0" x2="12" y2="8" stroke="#ffffff" stroke-width="2"/>
  </svg>
</body>
</html>
```